Hey Lunagraf, this time I go to you in direct demand :)
We need a Facebook Event Cover (High definition) :
- Name of the party "VELVET TIDE"
- Date of the party "Samedi 25 novembre"
- Place of the party "Brume7" (use logo please)
- DJ's: "K-Lenz + MV"
- Style of the flyer : Vintage
- Inspiration : Old vintage Ads, old vintage objects linked to music, inspiration on google images "Vintage party" "Retro Vintage party", should be really stylish :)
- Colors : You decide, you can try, pastel colors ?

```html
<!DOCTYPE html>
<html lang="fr">
<head>
<meta charset="utf-8">
<title>Velvet Tide – Samedi 25 novembre</title>
<link href="https://fonts.googleapis.com/css2?family=Bowlby+One&family=Russo+One&family=Montserrat:wght@300&display=swap" rel="stylesheet">
<style>
  :root{
    --cream:#f0d8bf;
    --ink:#2a140f;
    --red:#e6402b;
    --orange:#f27d2a;
    --yellow:#f6c11b;
    --olive:#3a3424;
    --tape-body:#c9b3a0;
    --tape-shade:#8f7d70;
  }
  *{margin:0;padding:0;box-sizing:border-box}
  html,body{width:1200px;height:628px;overflow:hidden;background:var(--olive)}
  .cover{position:relative;width:1200px;height:628px;overflow:hidden;
    background:linear-gradient(180deg,#3d2a22 0%,#3b3225 55%,var(--olive) 100%)}
  .stage-photo{position:absolute;inset:0 0 auto 0;height:430px;
    background:
      radial-gradient(ellipse 260px 200px at 120px 60px,rgba(214,70,50,.75),transparent 70%),
      radial-gradient(ellipse 300px 220px at 1080px 80px,rgba(214,60,45,.7),transparent 70%),
      radial-gradient(ellipse 240px 160px at 600px 40px,rgba(180,60,45,.6),transparent 70%),
      linear-gradient(180deg,rgba(70,35,30,.9),rgba(59,50,36,0));}
  .wave-band{position:absolute;left:0;top:180px;width:1200px;height:280px;
    background:linear-gradient(180deg,transparent,rgba(240,216,191,.08) 25%,rgba(240,216,191,.08) 75%,transparent)}
  .brand{position:absolute;top:86px;left:0;width:100%;text-align:center;
    font-family:"Montserrat",sans-serif;font-weight:300;font-size:42px;line-height:1;
    letter-spacing:8px;color:#fff;}
  .title{position:absolute;left:612px;top:292px;transform:translate(-50%,-50%) rotate(-5deg);
    padding:10px 40px 30px 30px;background:var(--cream);border-radius:40px;
    box-shadow:0 0 0 4px rgba(240,216,191,.55);}
  .title h1{font-family:"Bowlby One",sans-serif;font-weight:400;font-size:108px;line-height:1.05;
    white-space:nowrap;color:var(--cream);letter-spacing:1px;
    -webkit-text-stroke:6px var(--ink);paint-order:stroke fill;
    text-shadow:5px 6px 0 var(--ink),9px 11px 0 var(--red),13px 16px 0 var(--orange),17px 21px 0 var(--yellow);}
  .date{position:absolute;top:412px;left:0;width:100%;text-align:center;line-height:1;
    font-family:"Russo One",sans-serif;font-size:46px;color:var(--cream);letter-spacing:1px}
  .rule{position:absolute;top:477px;left:434px;width:350px;height:2px;background:var(--cream)}
  .lineup{position:absolute;top:492px;left:0;width:100%;text-align:center;line-height:1;
    font-family:"Russo One",sans-serif;font-size:74px;color:var(--cream);letter-spacing:2px}
  .note{position:absolute;fill:var(--cream)}
  .note-pair{left:1006px;top:112px;width:86px;height:80px}
  .note-small{left:1098px;top:222px;width:40px;height:70px}
  .note-left{left:140px;top:375px;width:62px;height:112px}
  .cassette{position:absolute;left:942px;top:368px;width:172px;height:108px;border-radius:10px;
    background:linear-gradient(160deg,var(--tape-body),var(--tape-shade));transform:rotate(12deg)}
</style>
</head>
<body>
<main class="cover">
  <div class="stage-photo" role="img" aria-label="Photo of a rock band playing live on stage under red and white spotlights"></div>
  <div class="wave-band" role="img" aria-label="Decorative pattern of thin horizontal wavy lines"></div>

  <div class="brand">BRUME7</div>

  <div class="title"><h1>VELVET TIDE</h1></div>

  <svg class="note note-pair" viewBox="0 0 86 80" aria-hidden="true">
    <path d="M24 14 L84 2 L84 14 L24 26 Z"/>
    <rect x="24" y="14" width="6" height="52"/>
    <rect x="78" y="4" width="6" height="52"/>
    <ellipse cx="16" cy="66" rx="15" ry="11" transform="rotate(-20 16 66)"/>
    <ellipse cx="70" cy="56" rx="15" ry="11" transform="rotate(-20 70 56)"/>
  </svg>
  <svg class="note note-small" viewBox="0 0 40 70" aria-hidden="true">
    <rect x="20" y="2" width="5" height="54"/>
    <path d="M25 2 C27 14 42 18 34 34 C36 22 30 18 25 16 Z"/>
    <ellipse cx="13" cy="58" rx="12" ry="9" transform="rotate(-20 13 58)"/>
  </svg>
  <svg class="note note-left" viewBox="0 0 62 112" aria-hidden="true">
    <rect x="30" y="2" width="7" height="88"/>
    <path d="M37 2 C40 22 66 28 52 56 C55 36 46 30 37 26 Z"/>
    <ellipse cx="19" cy="94" rx="18" ry="13" transform="rotate(-20 19 94)"/>
  </svg>

  <div class="cassette" role="img" aria-label="Illustration of a retro audio cassette with striped label"></div>

  <p class="date">SAMEDI 25 NOVEMBRE</p>
  <div class="rule"></div>
  <p class="lineup">K-LENZ + MV</p>
</main>
</body>
</html>
```